Steadying Downturn Worries

I need a on page electronic flyer for this coaching program. I want a silhouette to accompany the case the copy starts with. I have the copy written but need it put together in a striking way.

Target Market(s)

towards higher net worth individuals

Industry/Entity Type

Electronic

```html
<!DOCTYPE html>
<html lang="en">
<head>
<meta charset="utf-8">
<title>Steadying Downturn Worries</title>
<link href="https://fonts.googleapis.com/css2?family=Source+Sans+3:ital,wght@0,400;0,600;0,700;1,400&display=swap" rel="stylesheet">
<style>
  :root {
    --ink: #111111;
    --grey: #8a8a8a;
    --blue: #1a9ad6;
    --green: #8cc63f;
    --red: #e8262b;
    --gold: #f4c20d;
    --logo-blue: #1b7fc4;
    --paper: #ffffff;
  }
  * { margin: 0; padding: 0; box-sizing: border-box; }
  html, body { width: 843px; height: 1200px; overflow: hidden; background: var(--paper); }
  body { font-family: "Source Sans 3", "Myriad Pro", Arial, sans-serif; color: var(--ink); }
  .flyer { position: relative; width: 843px; height: 1200px; overflow: hidden; }
  .flyer > * { position: absolute; }

  .kicker { top: 2px; left: 0; width: 843px; text-align: center; font-size: 28px; color: var(--grey); letter-spacing: 0.3px; }
  .headline { top: 34px; left: 0; width: 843px; text-align: center; font-size: 58px; font-weight: 700; color: var(--blue); line-height: 1.1; }
  .subhead { top: 108px; left: 0; width: 843px; text-align: center; font-size: 39px; color: var(--green); line-height: 1.1; }

  .portrait { top: 172px; left: 30px; width: 184px; height: 192px; }
  .portrait-caption { top: 368px; left: 28px; font-size: 27px; }

  .case-story { top: 168px; left: 250px; width: 580px; font-size: 14.6px; font-style: italic; line-height: 1.25; text-align: center; }
  .case-story p + p { margin-top: 17px; }

  .lead-in { top: 410px; left: 0; width: 843px; text-align: center; font-size: 21px; color: var(--red); }
  .research { top: 440px; left: 24px; width: 800px; text-align: center; font-size: 14px; line-height: 1.3; }
  .question { top: 512px; left: 0; width: 843px; text-align: center; font-size: 21px; }

  .session-title { top: 551px; left: 5px; font-size: 19px; font-weight: 700; color: var(--green); }
  .session-list { top: 584px; left: 7px; list-style: none; font-size: 13.6px; line-height: 28px; }
  .session-list li::before { content: "\2022 "; }

  .program-title { top: 548px; left: 540px; font-size: 19px; font-weight: 700; color: var(--blue); }
  .program-list { top: 578px; left: 540px; list-style: none; font-size: 17px; line-height: 28px; }
  .program-list li::before { content: "\2022 "; }
  .guarantee { top: 669px; left: 474px; font-size: 20px; font-weight: 700; color: var(--gold); }

  .method { top: 730px; left: 5px; width: 830px; font-size: 17px; line-height: 29px; }

  .bio { top: 960px; left: 5px; width: 580px; font-size: 19.5px; line-height: 26px; color: var(--blue); }

  .contact { top: 1122px; left: 44px; font-size: 38px; }

  .brand { top: 928px; left: 603px; width: 224px; height: 224px; }
  .brand-mark { position: absolute; inset: 0; border-radius: 50%; background: var(--logo-blue); }
  .brand-name { position: absolute; top: 0; left: 0; width: 224px; height: 224px; display: flex; align-items: center; justify-content: center; text-align: center; font-size: 30px; font-weight: 600; line-height: 1.05; color: var(--paper); }
</style>
</head>
<body>
<main class="flyer">
  <p class="kicker">Sometimes the best financial advice isn't about numbers...</p>
  <h1 class="headline">Steadying Downturn Worries</h1>
  <h2 class="subhead">From Financial Worries to Wealth Satisfaction</h2>

  <svg class="portrait" viewBox="0 0 184 192" role="img" aria-label="Silhouette of a man from the shoulders up, representing Steven">
    <rect width="184" height="192" fill="#1a1a1a" opacity="0.9"/>
  </svg>
  <p class="portrait-caption">“Steven” Millbrook, PA</p>

  <div class="case-story">
    <p>A 49 year old attorney, Steve was used to success and rising net worth. But with huge losses in the market crash, layoffs at his firm, his kids heading for college and the stagnant economy stretching ahead, his usual optimism is gone.</p>
    <p>With his anxiety growing, Steve doubts his own decision making ability. His confidence slipping, he stopped opening his financial statements and could barely speak to his financial advisor. He thought if his advisor said “hang in there” one more time, he just might blow up.</p>
    <p>Yet Steve felt too embarrassed to talk about his deep worries, even with his wife. It seemed like all he could do was pour another glass of wine and suffer in isolation.</p>
  </div>

  <p class="lead-in">If you're like Steve, you're afraid and alone with plenty of company.</p>
  <p class="research">In a September 2009 National Wellbeing Council poll, 80 percent reported the economy is causing significant stress, up from 66 percent from the previous April. The Restful Nights Institute said 27 percent of people surveyed had sleeplessness because of economic anxiety.</p>
  <p class="question">How can you take control of these worries and get back to enjoying your life?</p>

  <h3 class="session-title">In this 5 session coaching process you will:</h3>
  <ul class="session-list">
    <li>Learn a decision making tool to make choices that truly serve your needs</li>
    <li>Clarify and more fully engage with your purpose and passions</li>
    <li>Improve your relationship with your financial advisor</li>
    <li>Feel more in control and confident in your financial life</li>
  </ul>

  <h3 class="program-title">A six week program to:</h3>
  <ul class="program-list">
    <li>Reduce stress</li>
    <li>Improve performance</li>
    <li>Restore Control</li>
  </ul>
  <p class="guarantee">$995 Money Back Guarantee</p>

  <div class="method">
    <p>This process guides you to step back and understand the source of your financial worry—your unique story about the meaning of money. Your money story drives your emotions and decision making—for better and worse. You'll learn a decision making tool for more conscious, effective and satisfying financial and life decisions.</p>
    <p>You'll also examine your core values and strengths—what really matters most to you and how you work at your best. When you use your money and your core strengths to pursue your highest aspirations, life and wealth become balanced. As you commit more fully to your mission and passions, satisfaction grows and money worries melt away.</p>
  </div>

  <p class="bio">Dale Morrow, Ph.D. is a psychologist with 30 years of experience treating anxiety and stress. He is co-founder and facilitator of Ledger Circle, a peer learning group for high net worth investors. For more information, call 267-555-0148.<br>dalemorrow@example.com</p>

  <p class="contact">Dale Morrow (215)555-0190</p>

  <div class="brand">
    <div class="brand-mark"></div>
    <span class="brand-name">Ledger<br>Circle</span>
  </div>
</main>
</body>
</html>
```